Packaging Design: Logo/Bottle Design for New Botanical Cocktail Brand

We are a new start up, looking to create a new line of Ready to drink Cocktails. The brand name is Verdelle Garden Cocktails, infused with fruit, herb, and floral botanicals grown on our farm in New Hampshire. Flavors will include: Herb flavored with cilantro, Berry- flavored with Alpine Strawberry, Citrus flavored with lemon Verbena & lemon balm, Pear flavored with Bartlett pear, Cucumber & Mint. We need a logo and a label design. There are 2 possible bottles to choose from.

Designer has complete freedom with everything! From fonts and colors to bottle caps and closures. Please view the pinterest link for inspirational bottle designs. https://www.pinboardly.example/kestrawynn/garden-drinks/

Target Market(s)

Female 21 to 48 years old. College educated and professional. The type of person that has a passion for a cause and eats and shops local. People that respect an artisan quality product, hand made by a master craftsman.

Industry/Entity Type

Floral

Requirements
Must have
• Clear Bottle, see options attached. You may also choose your own BUT WE MUST SEE THE LOGO AND IMAGERY ON A BOTTLE
• Logo Design: "Verdelle Garden Cocktails"
• Label: We can have front and back, or one continuous label. We are open to painted designs.
• The label must contain the following text in quotes:
• Product Name: " Verdelle Garden Cocktails "
• "15% Alc. by Vol. (30 proof)"
• "750 mL"
• "Handcrafted and Bottled by Harrow Creek Orchard Farm and Distillery
• Larkmoor, NH-USA"
• The following Text must be in all caps and 3mm in height:
• "Government Warning: (1) According to the Surgeon General, women should not drink alcoholic beverages during pregnancy because of the risk of birth defects. (2) Consumption of alcoholic beverages impairs your ability to drive a car or operate machinery and may cause health problems."
• Must be a space for a bar code: .75 in height by 1.25 in length.
• “www.harrowcreekorchard.example”
• Must Have the following Statement:
• Infused with fruit, herb, and floral botanicals and sweetened with stevia. Serve cold over ice.
Nice to have
• Antique or vintage botanical illustrations
• https://www.pinboardly.example/kestrawynn/garden-drinks/
• check out the board for inspiration.
• Think artisanal small batch spirits that are ready to drink out of the bottle. Refreshing flavors just pour over ice and add herb leaves.
• You can use images by doing a search here.
• http://archive.plantrecords.example/search.xhtml?start=0&collectionFacet=Orchard+Fruit+Painting+Set

```html
<!DOCTYPE html>
<html lang="en">
<head>
<meta charset="utf-8">
<title>Verdelle Garden Cocktails – Label Range</title>
<link rel="stylesheet" href="https://fonts.googleapis.com/css2?family=Roboto+Condensed:wght@400;700&family=Roboto+Slab:wght@400;700&display=swap">
<style>
  :root {
    --backdrop: #2d2c2e;
    --paper: #ffffff;
    --ink: #2a2a2a;
    --wordmark: #1f1d1e;
    --ribbon-dark: #2f2c2d;
    --ribbon-light: #6a6566;
    --citrus: #fdc82c;
    --herb: #a9cf46;
    --berry: #f4b2d3;
    --pear: #91d6f5;
    --cucumber: #e6e7e8;
  }
  * { margin: 0; padding: 0; box-sizing: border-box; }
  html, body { width: 1200px; height: 596px; overflow: hidden; background: var(--backdrop); }
  .range { position: relative; width: 1200px; height: 596px; }
  .label { position: absolute; top: 70px; width: 200px; height: 460px; color: var(--ink); text-align: center; }
  .label--citrus   { left: 63px;  --flavour: var(--citrus); }
  .label--herb     { left: 281px; --flavour: var(--herb); }
  .label--berry    { left: 498px; --flavour: var(--berry); }
  .label--pear     { left: 714px; --flavour: var(--pear); }
  .label--cucumber { left: 931px; --flavour: var(--cucumber); }
  .label__shape { position: absolute; inset: 0; }
  .label__shape .outer { fill: var(--paper); }
  .label__shape .inner { fill: var(--flavour); }
  .maker { position: absolute; top: 33px; left: 0; width: 200px; font-family: "Roboto Condensed", Arial, sans-serif; font-size: 7px; line-height: 12px; }
  .maker strong { font-weight: 700; display: block; }
  .brand { position: absolute; top: 82px; left: 20px; width: 160px; height: 84px; color: var(--wordmark); font-family: "Roboto Slab", Georgia, serif; font-weight: 700; display: flex; flex-direction: column; justify-content: center; line-height: 1.05; }
  .brand span { display: block; }
  .brand__top { font-size: 19px; }
  .brand__bottom { font-size: 29px; margin-top: 2px; }
  .site { position: absolute; top: 193px; left: 0; width: 200px; font-family: "Roboto Condensed", Arial, sans-serif; font-size: 7px; }
  .artwork { position: absolute; top: 235px; left: 47px; width: 106px; height: 118px; border-radius: 53px 53px 0 0; background: var(--paper); padding: 4px; }
  .artwork__fill { width: 100%; height: 100%; border-radius: 49px 49px 0 0; background: linear-gradient(180deg, #f2c6e2 0%, #e77fb8 30%, #9fc06a 60%, #e6c347 78%, #b6d36a 100%); }
  .ribbon { position: absolute; top: 336px; left: 20px; width: 160px; height: 46px; }
  .ribbon .band { fill: var(--ribbon-dark); }
  .ribbon .tail { fill: var(--ribbon-light); }
  .ribbon text { font-family: "Roboto Condensed", Arial, sans-serif; font-weight: 700; fill: #ffffff; letter-spacing: 1px; }
  .volume { position: absolute; top: 389px; left: 0; width: 200px; font-family: "Roboto Slab", Georgia, serif; font-size: 13px; }
</style>
</head>
<body>
<main class="range">

  <section class="label label--citrus">
    <svg class="label__shape" viewBox="0 0 200 460" width="200" height="460" aria-hidden="true">
      <path class="outer" d="M5,52 C20,20 60,8 100,8 C140,8 180,20 195,52 L183,452 L17,452 Z"/>
      <path class="inner" d="M13,58 C28,30 65,17 100,17 C135,17 172,30 187,58 L176,444 L24,444 Z"/>
    </svg>
    <p class="maker">Handcrafted and Bottled by<strong>Harrow Creek Orchard Farm and Distillery</strong>Larkmoor, NH-USA</p>
    <h2 class="brand"><span class="brand__top">Verdelle Garden</span><span class="brand__bottom">Cocktails</span></h2>
    <p class="site">www.harrowcreekorchard.example</p>
    <div class="artwork"><div class="artwork__fill" role="img" aria-label="Botanical illustration of pink lilies, herb leaves and a heap of fruit"></div></div>
    <svg class="ribbon" viewBox="0 0 160 46" aria-hidden="true">
      <path class="tail" d="M0,16 L18,14 L18,40 L4,42 L10,29 Z"/>
      <path class="tail" d="M160,10 L142,12 L142,36 L156,36 L150,23 Z"/>
      <path class="band" d="M10,10 Q80,0 150,6 L150,32 Q80,26 10,38 Z"/>
      <text x="80" y="28" font-size="20" text-anchor="middle" transform="rotate(-3 80 22)">CITRUS</text>
    </svg>
    <p class="volume">750 ML</p>
  </section>

  <section class="label label--herb">
    <svg class="label__shape" viewBox="0 0 200 460" width="200" height="460" aria-hidden="true">
      <path class="outer" d="M5,52 C20,20 60,8 100,8 C140,8 180,20 195,52 L183,452 L17,452 Z"/>
      <path class="inner" d="M13,58 C28,30 65,17 100,17 C135,17 172,30 187,58 L176,444 L24,444 Z"/>
    </svg>
    <p class="maker">Handcrafted and Bottled by<strong>Harrow Creek Orchard Farm and Distillery</strong>Larkmoor, NH-USA</p>
    <h2 class="brand"><span class="brand__top">Verdelle Garden</span><span class="brand__bottom">Cocktails</span></h2>
    <p class="site">www.harrowcreekorchard.example</p>
    <div class="artwork"><div class="artwork__fill" role="img" aria-label="Botanical illustration of pink lilies, herb leaves and a heap of fruit"></div></div>
    <svg class="ribbon" viewBox="0 0 160 46" aria-hidden="true">
      <path class="tail" d="M0,16 L18,14 L18,40 L4,42 L10,29 Z"/>
      <path class="tail" d="M160,10 L142,12 L142,36 L156,36 L150,23 Z"/>
      <path class="band" d="M10,10 Q80,0 150,6 L150,32 Q80,26 10,38 Z"/>
      <text x="80" y="28" font-size="20" text-anchor="middle" transform="rotate(-3 80 22)">HERB</text>
    </svg>
    <p class="volume">750 ML</p>
  </section>

  <section class="label label--berry">
    <svg class="label__shape" viewBox="0 0 200 460" width="200" height="460" aria-hidden="true">
      <path class="outer" d="M5,52 C20,20 60,8 100,8 C140,8 180,20 195,52 L183,452 L17,452 Z"/>
      <path class="inner" d="M13,58 C28,30 65,17 100,17 C135,17 172,30 187,58 L176,444 L24,444 Z"/>
    </svg>
    <p class="maker">Handcrafted and Bottled by<strong>Harrow Creek Orchard Farm and Distillery</strong>Larkmoor, NH-USA</p>
    <h2 class="brand"><span class="brand__top">Verdelle Garden</span><span class="brand__bottom">Cocktails</span></h2>
    <p class="site">www.harrowcreekorchard.example</p>
    <div class="artwork"><div class="artwork__fill" role="img" aria-label="Botanical illustration of pink lilies, herb leaves and a heap of fruit"></div></div>
    <svg class="ribbon" viewBox="0 0 160 46" aria-hidden="true">
      <path class="tail" d="M0,16 L18,14 L18,40 L4,42 L10,29 Z"/>
      <path class="tail" d="M160,10 L142,12 L142,36 L156,36 L150,23 Z"/>
      <path class="band" d="M10,10 Q80,0 150,6 L150,32 Q80,26 10,38 Z"/>
      <text x="80" y="28" font-size="20" text-anchor="middle" transform="rotate(-3 80 22)">BERRY</text>
    </svg>
    <p class="volume">750 ML</p>
  </section>

  <section class="label label--pear">
    <svg class="label__shape" viewBox="0 0 200 460" width="200" height="460" aria-hidden="true">
      <path class="outer" d="M5,52 C20,20 60,8 100,8 C140,8 180,20 195,52 L183,452 L17,452 Z"/>
      <path class="inner" d="M13,58 C28,30 65,17 100,17 C135,17 172,30 187,58 L176,444 L24,444 Z"/>
    </svg>
    <p class="maker">Handcrafted and Bottled by<strong>Harrow Creek Orchard Farm and Distillery</strong>Larkmoor, NH-USA</p>
    <h2 class="brand"><span class="brand__top">Verdelle Garden</span><span class="brand__bottom">Cocktails</span></h2>
    <p class="site">www.harrowcreekorchard.example</p>
    <div class="artwork"><div class="artwork__fill" role="img" aria-label="Botanical illustration of pink lilies, herb leaves and a heap of fruit"></div></div>
    <svg class="ribbon" viewBox="0 0 160 46" aria-hidden="true">
      <path class="tail" d="M0,16 L18,14 L18,40 L4,42 L10,29 Z"/>
      <path class="tail" d="M160,10 L142,12 L142,36 L156,36 L150,23 Z"/>
      <path class="band" d="M10,10 Q80,0 150,6 L150,32 Q80,26 10,38 Z"/>
      <text x="80" y="28" font-size="20" text-anchor="middle" transform="rotate(-3 80 22)">PEAR</text>
    </svg>
    <p class="volume">750 ML</p>
  </section>

  <section class="label label--cucumber">
    <svg class="label__shape" viewBox="0 0 200 460" width="200" height="460" aria-hidden="true">
      <path class="outer" d="M5,52 C20,20 60,8 100,8 C140,8 180,20 195,52 L183,452 L17,452 Z"/>
      <path class="inner" d="M13,58 C28,30 65,17 100,17 C135,17 172,30 187,58 L176,444 L24,444 Z"/>
    </svg>
    <p class="maker">Handcrafted and Bottled by<strong>Harrow Creek Orchard Farm and Distillery</strong>Larkmoor, NH-USA</p>
    <h2 class="brand"><span class="brand__top">Verdelle Garden</span><span class="brand__bottom">Cocktails</span></h2>
    <p class="site">www.harrowcreekorchard.example</p>
    <div class="artwork"><div class="artwork__fill" role="img" aria-label="Botanical illustration of pink lilies, herb leaves and a heap of fruit"></div></div>
    <svg class="ribbon" viewBox="0 0 160 46" aria-hidden="true">
      <path class="tail" d="M0,16 L18,14 L18,40 L4,42 L10,29 Z"/>
      <path class="tail" d="M160,10 L142,12 L142,36 L156,36 L150,23 Z"/>
      <path class="band" d="M10,10 Q80,0 150,6 L150,32 Q80,26 10,38 Z"/>
      <text x="80" y="27" font-size="16" text-anchor="middle" transform="rotate(-3 80 22)">CUCUMBER</text>
    </svg>
    <p class="volume">750 ML</p>
  </section>

</main>
</body>
</html>
```